Tidewell Giving Fund - New Website Designed

I need a site that looks like this http://www.ridgelanegiving.org for boat donations. So please replace the cars with boats.

```html
<!DOCTYPE html>
<html lang="en">
<head>
<meta charset="utf-8">
<title>Tidewell Giving Fund – Donate Your Boat</title>
<link rel="stylesheet" href="https://fonts.googleapis.com/css2?family=Roboto:wght@300;400;500;700&family=Montserrat:wght@700&display=swap">
<style>
:root{
  --navy:#1d4a7c;
  --blue:#1f7bc1;
  --blue-deep:#1760a4;
  --band:#2f7fc0;
  --red:#d9101a;
  --red-dark:#b20c14;
  --ink:#222;
  --muted:#555;
  --heading:#1d4f86;
  --grey-panel:#ebebeb;
  --faq-bg:#e9f3fa;
  --faq-btn:#2c6496;
  --footer:#20587f;
  --white:#fff;
}
*{box-sizing:border-box;margin:0;padding:0}
html,body{width:1200px;height:2439px;overflow:hidden}
body{font-family:"Roboto",sans-serif;color:var(--ink);background:var(--white);position:relative}
.abs{position:absolute}

/* header */
.topbar{left:0;top:0;width:1200px;height:98px;background:linear-gradient(90deg,#1c3d68,#2a5587 60%,#35629a)}
.brand{left:100px;top:30px;display:flex;align-items:center;gap:12px;color:var(--white);font-size:26px;font-weight:500;letter-spacing:.3px}
.brand-mark{width:30px;height:30px;border-radius:50%;background:var(--white)}
.callbox{left:771px;top:0;width:330px;height:98px;background:var(--red);color:var(--white);text-align:center;padding-top:12px}
.callbox .lbl{font-size:14px;letter-spacing:.5px}
.callbox .num{font-size:29px;font-weight:400;margin-top:2px}
.callbox .sub{font-size:11px;margin-top:2px}
.navbar{left:0;top:98px;width:1200px;height:53px;background:var(--blue)}
.nav{left:99px;top:98px;height:53px;display:flex;align-items:center;gap:31px;list-style:none}
.nav li{color:var(--white);font-size:14px;font-weight:500}
.donate-online{left:758px;top:98px;width:356px;height:53px;background:var(--blue-deep);color:var(--white);font-size:20px;display:flex;align-items:center;justify-content:center}

/* hero */
.hero{left:0;top:151px;width:1200px;height:495px;background:linear-gradient(180deg,#9fc6e6 0%,#cfe3f2 55%,#e4eef5 100%)}
.hero-photo{left:40px;top:151px;width:700px;height:495px;background:radial-gradient(ellipse at 45% 55%,#8d8a78 0%,#7a7f73 35%,rgba(150,170,180,.0) 72%)}
.dots{left:562px;top:610px;display:flex;gap:10px}
.dots span{width:9px;height:9px;border-radius:50%;background:var(--white)}
.dots span.on{background:var(--red)}
.form-card{left:771px;top:151px;width:330px;height:413px}
.form-inner{left:771px;top:151px;width:330px;padding:26px 40px 0}
.form-title{color:var(--white);font-size:12.5px;font-weight:700;text-align:center;margin-bottom:14px}
.field{background:var(--white);height:28px;font-size:9px;color:#777;padding:9px 10px;margin-bottom:10px}
.row{display:flex;gap:10px}
.row .field{flex:1}
.select{position:relative}
.select::after{content:"";position:absolute;right:10px;top:12px;border:5px solid transparent;border-top-color:#333}
.btn-donate{display:block;margin:14px auto 0;width:118px;height:33px;background:var(--blue-deep);color:var(--white);font-size:12px;text-align:center;line-height:33px}
.thanks{color:var(--white);font-size:10px;font-style:italic;text-align:center;margin-top:8px}

/* features */
.feature-lead{left:99px;top:646px;width:381px;height:232px;background:linear-gradient(135deg,#2c7fc2,#1d6fb2);color:var(--white);padding:38px 0 0 58px}
.feature-lead .l1{font-size:26px;font-weight:300}
.feature-lead .l2{font-size:60px;font-weight:300;line-height:1.05}
.feature-lead .l3{font-size:30px;font-weight:300}
.feature-grid{left:480px;top:657px;width:621px;height:208px;background:var(--grey-panel);display:flex;padding:42px 10px 0 18px}
.feature{width:108px;text-align:center;font-size:12.5px;color:#333;line-height:1.3}
.feature svg{display:block;margin:0 auto 12px}
.fold{left:480px;top:865px}

/* how */
.h2{font-size:27px;font-weight:400;color:var(--heading);text-align:center;width:1200px;left:0}
.h2 b{color:var(--red);font-weight:500}
.step{display:flex;gap:14px;width:300px}
.step h3{font-size:16px;font-weight:700;color:var(--heading)}
.step .tel{font-size:13px;font-weight:700;margin-top:2px}
.step p{font-size:11px;color:var(--muted);line-height:1.45;margin-top:3px}

/* why */
.why{left:0;top:1150px;width:1200px;height:421px;background:linear-gradient(90deg,#2a6eac,#3a86c4 50%,#2a74b4)}
.why-title{left:0;top:1176px;width:1200px;text-align:center;color:var(--white);font-size:25px;font-weight:400}
.why-list{left:276px;top:1270px;list-style:none}
.why-list li{color:var(--white);font-size:13px;height:41px;display:flex;align-items:center;gap:18px}

/* faq */
.faq-photo{left:99px;top:1672px;width:492px;height:344px;background:linear-gradient(135deg,#b8a58c,#8d7c68 45%,#6a6a55)}
.faq{left:605px;top:1672px;width:496px}
.q{height:39px;background:var(--faq-bg);border-radius:5px;display:flex;align-items:center;justify-content:space-between;font-size:14.5px;color:#222;margin-bottom:13px;overflow:hidden}
.q span{padding-left:16px}
.q i{width:41px;height:39px;background:var(--faq-btn);color:var(--white);font-style:normal;display:flex;align-items:center;justify-content:center;font-size:18px}
.q-open{background:var(--faq-btn);border-radius:5px;margin-bottom:13px}
.q-open .q{margin:0;border-radius:5px 5px 0 0}
.q-open p{color:var(--white);font-size:12px;line-height:1.5;padding:12px 16px 16px}

/* secure */
.secure{left:0;top:2052px;width:1200px;height:115px;display:flex;align-items:center;justify-content:center;gap:40px}
.secure .txt{font-family:"Montserrat",sans-serif;font-size:26px;color:var(--heading);font-weight:700;margin-right:0}
.badge-shield{width:170px;height:80px}
.badge-seal{width:100px;height:86px}

/* footer */
.footer{left:0;top:2167px;width:1200px;height:272px;background:linear-gradient(180deg,#2a6690,#1c4f74)}
.fcol h4{color:var(--white);font-size:17px;font-weight:400;margin-bottom:18px}
.flinks{list-style:none}
.flinks li{color:var(--white);font-size:11.5px;height:31px;display:flex;align-items:center;gap:10px}
.flinks li::before{content:"";width:11px;height:11px;border-radius:50%;background:var(--white)}
.about p{color:var(--white);font-size:11.5px;line-height:1.6;text-align:justify}
.email{width:226px;height:34px;background:var(--white);border-radius:6px;font-size:11.5px;color:#888;padding:10px 16px}
.sub-btn{margin-top:10px;width:130px;height:32px;background:var(--red);color:var(--white);border-radius:6px;font-size:13px;font-weight:500;text-align:center;line-height:32px}
.social{display:flex;gap:12px}
.social span{width:24px;height:24px;border-radius:2px}
.foot-brand{color:var(--white);font-size:12.5px;font-weight:500;display:flex;align-items:center;gap:8px}
.foot-brand i{width:14px;height:14px;border-radius:50%;background:var(--white)}
.foot-rule{left:99px;top:2395px;width:1002px;height:1px;background:rgba(255,255,255,.25)}
.copy{left:0;top:2408px;width:1200px;text-align:center;color:var(--white);font-size:11.5px}
</style>
</head>
<body>

<header>
  <div class="abs topbar"></div>
  <div class="abs brand"><span class="brand-mark"></span>TIDEWELL GIVING FUND</div>
  <div class="abs callbox">
    <div class="lbl">CALL TODAY TO DONATE</div>
    <div class="num">1-800-555-0148</div>
    <div class="sub">Live operators - 7 days a week</div>
  </div>
  <div class="abs navbar"></div>
  <ul class="abs nav">
    <li>HOW TO DONATE</li><li>WHY DONATE</li><li>FAQ</li><li>ABOUT</li>
  </ul>
  <div class="abs donate-online">DONATE YOUR BOAT ONLINE</div>
</header>

<section>
  <div class="abs hero"></div>
  <div class="abs hero-photo" role="img" aria-label="Soldier in uniform hugging a small child against a blue sky"></div>
  <div class="abs dots"><span></span><span></span><span class="on"></span><span></span></div>
  <svg class="abs form-card" viewBox="0 0 330 413" aria-hidden="true"><polygon points="0,0 330,0 330,360 165,413 0,360" fill="#d9101a"/></svg>
  <div class="abs form-inner">
    <div class="form-title">FULL TAX DEDUCTION - RUNNING OR NOT</div>
    <div class="row"><div class="field">First Name</div><div class="field">Last Name</div></div>
    <div class="field">Email</div>
    <div class="field">Day time Phone</div>
    <div class="field">Zip Code</div>
    <div class="row"><div class="field select">Choose Year</div><div class="field select">Choose Make</div></div>
    <div class="field">Model of boat</div>
    <span class="btn-donate">DONATE NOW</span>
    <div class="thanks">Thank You for Your Donation!</div>
  </div>
</section>

<section>
  <div class="abs feature-lead">
    <div class="l1">Donate Your Boats To</div>
    <div class="l2">Veterans</div>
    <div class="l3">Make a Difference</div>
  </div>
  <div class="abs feature-grid">
    <div class="feature"><svg width="56" height="56" viewBox="0 0 56 56" fill="none" stroke="#1d4f86" stroke-width="3"><circle cx="28" cy="28" r="24"/><path d="M17 29l8 8 16-18"/></svg>You have<br>no costs</div>
    <div class="feature"><svg width="70" height="56" viewBox="0 0 70 56" fill="none" stroke="#1d4f86" stroke-width="2.5"><rect x="4" y="22" width="34" height="18"/><path d="M38 26h14l8 10v4H38z"/><path d="M20 22l10-16"/><circle cx="14" cy="44" r="5"/><circle cx="48" cy="44" r="5"/></svg>Free towing,<br>running or not</div>
    <div class="feature"><svg width="56" height="56" viewBox="0 0 56 56" fill="none" stroke="#1d4f86" stroke-width="2.5"><path d="M12 4h32v48l-5-4-5 4-6-4-6 4-5-4-5 4z"/><path d="M18 14h20M18 22h12M18 30h10"/><text x="36" y="38" font-size="14" fill="#1d4f86" stroke="none" font-family="Roboto,sans-serif">$</text></svg>We issue you an<br>IRS tax receipt</div>
    <div class="feature"><svg width="56" height="56" viewBox="0 0 56 56" fill="none" stroke="#1d4f86" stroke-width="2.5"><rect x="20" y="6" width="30" height="40"/><path d="M26 14h18M34 22h10M34 30h10"/><circle cx="20" cy="30" r="10"/><path d="M12 38L4 48"/></svg>We take care of<br>all paperwork</div>
    <div class="feature"><svg width="56" height="56" viewBox="0 0 56 56" fill="none" stroke="#1d4f86" stroke-width="2.5"><path d="M12 4h24l10 10v38H12z"/><path d="M36 4v10h10"/><path d="M29 16v18M22 26l7 8 7-8M20 42h18"/></svg>We take care of<br>DMV &amp; Smog issues</div>
  </div>
  <svg class="abs fold" width="621" height="22" viewBox="0 0 621 22" aria-hidden="true"><polygon points="0,0 14,0 0,12" fill="#111"/><path d="M330 0 H621 L600 18 Q460 8 330 0Z" fill="rgba(0,0,0,.08)"/></svg>
</section>

<section>
  <h2 class="abs h2" style="top:918px">How To <b>Donate</b></h2>
  <div class="abs step" style="left:127px;top:998px">
    <svg width="50" height="50" viewBox="0 0 50 50" fill="none" stroke="#d9101a" stroke-width="2.5"><circle cx="27" cy="25" r="18"/><path d="M9 25h36M27 7c-8 10-8 26 0 36M27 7c8 10 8 26 0 36"/><path d="M4 30c2 8 8 14 14 16" stroke-width="5"/></svg>
    <div><h3>CALL US</h3><div class="tel">TOLL-FREE 1-800-555-0148</div><p>Excepteur sint occaecat cupidatat non proident, sunt in culpa.</p></div>
  </div>
  <div class="abs step" style="left:442px;top:988px">
    <svg width="76" height="44" viewBox="0 0 76 44" fill="none" stroke="#d9101a" stroke-width="2.5"><path d="M4 30l50-22 18 4v6l-18 10H4z"/><circle cx="18" cy="34" r="5"/><circle cx="56" cy="30" r="5"/><path d="M4 8h24"/></svg>
    <div><h3>WE TOW IT</h3><p>Excepteur sint occaecat cupidatat non proident, sunt in culpa qui officia deserunt mollit anim id est laborum.</p></div>
  </div>
  <div class="abs step" style="left:785px;top:988px">
    <svg width="46" height="56" viewBox="0 0 46 56" fill="none" stroke="#d9101a" stroke-width="2.5"><path d="M4 4h26l10 10v38H4z"/><text x="9" y="30" font-size="12" font-weight="700" fill="#d9101a" stroke="none" font-family="Roboto,sans-serif">TAX</text><circle cx="32" cy="44" r="8"/><path d="M28 44l3 3 5-6"/></svg>
    <div><h3>TAX WRITE OFF</h3><p>Excepteur sint occaecat cupidatat non proident, sunt in culpa qui officia deserunt mollit anim id est laborum.</p></div>
  </div>
</section>

<section>
  <div class="abs why" role="img" aria-label="Smiling soldier embracing family, tinted blue"></div>
  <h2 class="abs why-title">Why donate your Boat to us</h2>
  <svg class="abs" style="left:563px;top:1218px" width="74" height="24" viewBox="0 0 74 24" aria-hidden="true"><path d="M2 14h60l10-8-6 14H10z" fill="#fff"/><path d="M24 14V6h22l6 8" fill="none" stroke="#fff" stroke-width="2.5"/></svg>
  <ul class="abs why-list">
    <li><svg width="14" height="14" viewBox="0 0 14 14"><circle cx="7" cy="7" r="7" fill="#fff"/><path d="M3.5 7l2.5 2.5 4.5-5" stroke="#2a74b4" stroke-width="1.8" fill="none"/></svg>Excepteur sint occaecat cupidatat non proident, sunt in culpa qui officia deserunt mollit anim id est laborum</li>
    <li><svg width="14" height="14" viewBox="0 0 14 14"><circle cx="7" cy="7" r="7" fill="#fff"/><path d="M3.5 7l2.5 2.5 4.5-5" stroke="#2a74b4" stroke-width="1.8" fill="none"/></svg>Duis aute irure dolor in reprehenderit in voluptate velit esse cillum dolore eu fugiat nulla pariatur</li>
    <li><svg width="14" height="14" viewBox="0 0 14 14"><circle cx="7" cy="7" r="7" fill="#fff"/><path d="M3.5 7l2.5 2.5 4.5-5" stroke="#2a74b4" stroke-width="1.8" fill="none"/></svg>Nemo enim ipsam voluptatem quia voluptas sit aspernatur aut odit aut fugit,</li>
    <li><svg width="14" height="14" viewBox="0 0 14 14"><circle cx="7" cy="7" r="7" fill="#fff"/><path d="M3.5 7l2.5 2.5 4.5-5" stroke="#2a74b4" stroke-width="1.8" fill="none"/></svg>Quis autem vel eum iure reprehenderit qui in ea voluptate velit esse</li>
    <li><svg width="14" height="14" viewBox="0 0 14 14"><circle cx="7" cy="7" r="7" fill="#fff"/><path d="M3.5 7l2.5 2.5 4.5-5" stroke="#2a74b4" stroke-width="1.8" fill="none"/></svg>Nam libero tempore, cum soluta nobis est eligendi optio cumque nihil impedit quo</li>
    <li><svg width="14" height="14" viewBox="0 0 14 14"><circle cx="7" cy="7" r="7" fill="#fff"/><path d="M3.5 7l2.5 2.5 4.5-5" stroke="#2a74b4" stroke-width="1.8" fill="none"/></svg>Temporibus autem quibusdam et aut officiis debitis aut rerum necessitatibus saepe eveniet</li>
  </ul>
</section>

<section>
  <h2 class="abs h2" style="top:1605px">Frequently asked <b>questions</b></h2>
  <div class="abs faq-photo" role="img" aria-label="Mother in camouflage uniform hugging her child at home"></div>
  <div class="abs faq">
    <div class="q"><span>Duis aute irure dolor in reprehenderit in voluptate ?</span><i>+</i></div>
    <div class="q-open">
      <div class="q"><span>Duis aute irure dolor in reprehenderit in voluptate ?</span><i>-</i></div>
      <p>Neque porro quisquam est, qui dolorem ipsum quia dolor sit amet, consectetur, adipisci velit, sed quia non numquam eius ....</p>
    </div>
    <div class="q"><span>Duis aute irure dolor in reprehenderit in voluptate ?</span><i>+</i></div>
    <div class="q"><span>Duis aute irure dolor in reprehenderit in voluptate ?</span><i>+</i></div>
    <div class="q"><span>Duis aute irure dolor in reprehenderit in voluptate ?</span><i>+</i></div>
  </div>
</section>

<section class="abs secure">
  <div class="txt">SAFE &amp; SECURE</div>
  <svg class="badge-shield" viewBox="0 0 170 80" aria-label="Security badge"><rect x="0" y="5" width="170" height="70" rx="8" fill="#d9101a"/></svg>
  <svg class="badge-seal" viewBox="0 0 100 86" aria-label="Charity certification badge"><circle cx="50" cy="43" r="40" fill="#3d8fc9"/><circle cx="50" cy="43" r="30" fill="#e6eef5"/></svg>
</section>

<footer>
  <div class="abs footer" role="img" aria-label="Pine forest tinted blue"></div>
  <div class="abs fcol" style="left:99px;top:2197px">
    <h4>Navigation</h4>
    <ul class="flinks"><li>How to donate</li><li>Why donate</li><li>FAQ</li><li>About</li></ul>
  </div>
  <div class="abs fcol about" style="left:306px;top:2197px;width:240px">
    <h4>About Us</h4>
    <p>Temporibus autem quibusdam et aut officiis debitis aut rerum necessitatibus saepe eveniet ut et voluptates repudiandae sint et molestiae non recusandae. Itaque earum rerum hic tenetur a sapiente delectus, ut aut reiciendis voluptatibus maiores alias consequatur</p>
  </div>
  <div class="abs fcol" style="left:623px;top:2197px">
    <h4>Newsletter Subscription</h4>
    <div class="email">Enter Email id</div>
    <div class="sub-btn">Subscribe Now</div>
  </div>
  <div class="abs fcol" style="left:966px;top:2197px">
    <h4>Follow Us</h4>
    <div class="social"><span style="background:#3b5a98"></span><span style="background:#2aa6dc"></span><span style="background:#cf4332"></span><span style="background:#6b4a3a"></span></div>
    <div class="foot-brand" style="margin-top:26px"><i></i>TIDEWELL GIVING FUND</div>
  </div>
  <div class="abs foot-rule"></div>
  <div class="abs copy">© Copyright 2017 : www.companyname.com | All rights reserved</div>
</footer>

</body>
</html>
```